Brochure for a website accessibility report

This brochure is related to a report that www.kelvat.org sell. The report shows the results of an automated audit of a websites accessibility. It shows details of issues found with screen shots, examples of code and provides remediation advice.

The brochure will be a pdf 8.5 inches by 11 inches. It can be anywhere from 6 to 10 pages.

The FaultLens™ name itself should be “Bree Serif” font. The fonts, styles, colors and sizes are up to you.

The images used and logo of the Office of Digital Openness and Q7N logo are upload

We highlighted in blue page extracts from the report we sell. Do not use the blue highlight, it is merely there to show you where the specific examples of the report we sell are vs the other content in the report. The areas in blue which show the content from the actual report should be shown as an extract of the actual page of the report. You have flexibility to change the layout and the way the content look.

The red square callouts over the blue content are callouts that describe the specific page extracts. We used it as a red callout only so that you would be able to see it. You should change the specific location, look and feel of the callout to be appropriate

Target Market(s)

Marketing and Technical people

Industry/Entity Type

Information Technology

Font styles to use
Sans Serif

Colors

Designer to choose colors to be used in the design.

Requirements
Should not have
• wheelchairs, images of blind people

```html
<!DOCTYPE html>
<html lang="en">
<head>
<meta charset="utf-8">
<title>FaultLens™ Brochure Cover</title>
<link rel="stylesheet" href="https://fonts.googleapis.com/css2?family=Bree+Serif&family=Raleway:wght@400;500;700&display=swap">
<style>
  :root {
    --backdrop: #e3e3e3;
    --paper: #f4f4f4;
    --ink: #151515;
    --green: #2eaa62;
    --green-light: #4cc27c;
    --navy: #1f3566;
    --photo-deep: #3f4a57;
    --photo-dark: #5a6673;
    --photo-mid: #8d98a4;
    --photo-light: #d3d9df;
    --glow: rgba(255,255,255,0.85);
    --white: #ffffff;
  }
  * { box-sizing: border-box; margin: 0; padding: 0; }
  html, body {
    width: 1200px;
    height: 840px;
    overflow: hidden;
    background: var(--backdrop);
    font-family: "Raleway", Arial, sans-serif;
  }
  .cover {
    position: absolute;
    left: 300px;
    top: 32px;
    width: 600px;
    height: 776px;
    background: var(--paper);
    box-shadow: 0 8px 24px rgba(0,0,0,0.18);
    overflow: hidden;
  }
  .masthead {
    position: absolute;
    left: 0; top: 0;
    width: 600px;
    height: 200px;
    background: var(--paper);
  }
  .org-name {
    position: absolute;
    left: 40px;
    top: 38px;
    display: flex;
    align-items: flex-start;
    gap: 16px;
  }
  .org-name__square {
    width: 52px;
    height: 52px;
    background: var(--green);
    flex: none;
    margin-top: 2px;
  }
  .org-name__text {
    font-family: "Bree Serif", Georgia, serif;
    font-size: 27px;
    line-height: 0.98;
    text-transform: uppercase;
    color: var(--ink);
  }
  .seal {
    position: absolute;
    left: 352px;
    top: 104px;
    width: 74px;
    height: 74px;
    border-radius: 50%;
    background: var(--navy);
  }
  .mission {
    position: absolute;
    left: 438px;
    top: 100px;
    width: 146px;
    color: var(--navy);
  }
  .mission__head {
    display: flex;
    align-items: center;
    gap: 8px;
  }
  .mission__rule {
    flex: 1;
    height: 1px;
    background: var(--green);
  }
  .mission__quote-mark {
    font-family: "Bree Serif", Georgia, serif;
    color: var(--green);
    font-size: 22px;
    line-height: 0.6;
  }
  .mission__text {
    margin-top: 8px;
    font-size: 11px;
    line-height: 1.3;
  }
  .mission__foot {
    margin-top: 6px;
    display: flex;
    align-items: center;
    gap: 6px;
    font-size: 10px;
    font-weight: 700;
  }
  .mission__foot .mission__rule { max-width: 50px; }
  .hero-photo {
    position: absolute;
    left: 0; top: 200px;
    width: 600px;
    height: 576px;
    background:
      radial-gradient(ellipse 120px 90px at 38% 30%, var(--photo-light) 0%, transparent 100%),
      radial-gradient(ellipse 260px 200px at 40% 34%, rgba(211,217,223,0.55) 0%, transparent 100%),
      radial-gradient(ellipse 220px 300px at 70% 70%, var(--photo-deep) 0%, transparent 100%),
      radial-gradient(ellipse 180px 260px at 15% 60%, rgba(63,74,87,0.7) 0%, transparent 100%),
      linear-gradient(165deg, var(--photo-mid) 0%, var(--photo-dark) 55%, var(--photo-mid) 100%);
  }
  .hero-icons {
    position: absolute;
    left: 0; top: 200px;
    width: 600px;
    height: 576px;
  }
  .product-name {
    position: absolute;
    right: 38px;
    top: 228px;
    font-family: "Bree Serif", Georgia, serif;
    font-size: 68px;
    line-height: 1;
    color: var(--white);
    text-shadow: 0 0 14px rgba(255,255,255,0.35);
  }
  .edition-band {
    position: absolute;
    left: 0;
    top: 690px;
    width: 600px;
    height: 70px;
    background: var(--green);
  }
  .edition-band__notch {
    position: absolute;
    left: 0; top: 0;
  }
  .edition-band__title {
    position: absolute;
    left: 70px;
    top: 9px;
    font-family: "Bree Serif", Georgia, serif;
    font-size: 28px;
    line-height: 1;
    color: var(--white);
  }
  .edition-band__subtitle {
    position: absolute;
    left: 70px;
    top: 44px;
    font-size: 12px;
    font-weight: 500;
    letter-spacing: 0.04em;
    text-transform: uppercase;
    color: var(--ink);
  }
  .edition-band__contact {
    position: absolute;
    right: 0; top: 0;
    width: 170px;
    height: 70px;
    background: var(--green-light);
    padding: 9px 14px 0 14px;
    text-align: right;
    color: var(--white);
  }
  .edition-band__url {
    font-size: 14px;
    font-weight: 700;
  }
  .edition-band__mission {
    margin-top: 3px;
    font-size: 8.5px;
    line-height: 1.25;
  }
</style>
</head>
<body>
  <main class="cover">
    <header class="masthead">
      <div class="org-name">
        <span class="org-name__square"></span>
        <span class="org-name__text">Office of<br>Digital<br>Openness</span>
      </div>
      <div class="seal" role="img" aria-label="Partner seal"></div>
      <aside class="mission">
        <div class="mission__head"><span class="mission__quote-mark">“</span><span class="mission__rule"></span></div>
        <p class="mission__text">The mission of the ODO team is to make the Internet accessible for everyone.</p>
        <div class="mission__foot"><span class="mission__rule"></span><span>www.kelvat.org</span><span class="mission__quote-mark">”</span></div>
      </aside>
    </header>

    <div class="hero-photo" role="img" aria-label="Photo of a businessman in a grey suit touching glowing interface icons on a virtual screen"></div>

    <svg class="hero-icons" viewBox="0 0 600 576" aria-hidden="true">
      <g fill="none" stroke="#ffffff" stroke-width="5" stroke-linejoin="round" stroke-linecap="round" opacity="0.85">
        <!-- arrow tile -->
        <rect x="30" y="300" width="74" height="64" rx="8"/>
        <path d="M48 348 L84 316 M66 316 H84 V334"/>
        <!-- search tile -->
        <rect x="250" y="440" width="96" height="84" rx="8"/>
        <circle cx="292" cy="476" r="20"/>
        <path d="M306 490 L326 510"/>
        <!-- grid tile -->
        <rect x="60" y="430" width="80" height="70" rx="8" opacity="0.5"/>
        <path d="M80 450 H120 M80 466 H120 M80 482 H108" opacity="0.5"/>
      </g>
      <g fill="#ffffff" opacity="0.9">
        <!-- chat tile -->
        <rect x="40" y="150" width="90" height="70" rx="8" opacity="0.75"/>
        <!-- speech bubbles -->
        <path d="M300 330 a46 36 0 1 1 30 34 l-28 14 l8 -22 a46 36 0 0 1 -10 -26 z"/>
        <path d="M370 318 a40 32 0 1 1 -6 60 l20 20 l-34 -14 a40 32 0 0 1 20 -66 z" opacity="0.85"/>
      </g>
      <g fill="none" stroke="#ffffff" stroke-width="2" opacity="0.35">
        <path d="M0 250 H600 M0 410 H600"/>
      </g>
    </svg>

    <h1 class="product-name">FaultLens™</h1>

    <section class="edition-band">
      <svg class="edition-band__notch" width="52" height="70" viewBox="0 0 52 70" aria-hidden="true">
        <polygon points="14,0 52,0 30,34 14,34" fill="#ffffff"/>
      </svg>
      <h2 class="edition-band__title">2019 Brochure</h2>
      <p class="edition-band__subtitle">Office of Digital Openness</p>
      <div class="edition-band__contact">
        <p class="edition-band__url">www.kelvat.org</p>
        <p class="edition-band__mission">The mission of the ODO team is to make the Internet accessible for everyone.</p>
      </div>
    </section>
  </main>
</body>
</html>
```